LQV Web Site

Build a web site for Distant Charting and Rostering (LQV)

Target Market(s)

Petrochemical, Refining, and Manufacturing

Industry/Entity Type

Manufacturing

Coding

Coded - Design and coding required

Number of Pages Required

1 page

Font styles to use
Sans Serif

Colors

Designer to choose only greyscale colors for use in the design.

Requirements
Must have
• LQV is a member of WEN Venture Services family of companies, along with Brivonta, and Mulvarde.
Would like LQV to mimic Brivonta, and Mulvarde in layout and functionality.
WIll use the same office address and phone # found Brivonta and Mulvarde.
The color scheme needs to match the logo colors.
The final product needs to be in word press.
would like to connect the QR code found on one-pager to the website.

Reference these websites: www.brivonta-example.com and www.mulvarde-example.com
Nice to have
• Would like to have a contact tab similar to the one found on Mulvarde website. Use this email address. (LQV@WEN.example.com)
The home page needs to have simple depictions of the problem statement, solution, and introduction to LQV. (use the video script to help, feel free to use your own words)

```html
<!DOCTYPE html>
<html lang="en">
<head>
<meta charset="utf-8">
<title>LQV – Distant Charting and Rostering</title>
<link href="https://fonts.googleapis.com/css2?family=Nunito:ital,wght@0,400;0,600;0,700;0,800;1,400;1,600;1,800&display=swap" rel="stylesheet">
<style>
:root{
  --blue:#2e9fd6;
  --blue-soft:#dcebf3;
  --ink:#1b1b1b;
  --text:#3d3d3d;
  --grey-band:#f3f3f3;
  --step-a:#dbe6ee;
  --step-b:#e4e8ef;
  --cta-band:#eef2f7;
  --white:#ffffff;
}
*{box-sizing:border-box;margin:0;padding:0}
html,body{width:1200px;height:4284px;overflow:hidden}
body{position:relative;font-family:"Nunito",sans-serif;color:var(--text);background:var(--white)}
.abs{position:absolute}
.btn{position:absolute;background:var(--blue);color:var(--white);font-size:15px;display:flex;align-items:center;justify-content:center;gap:8px}
.brand{display:flex;align-items:center;gap:10px;font-weight:800;color:var(--blue);font-size:40px;letter-spacing:2px}
.brand-dot{width:22px;height:22px;border-radius:50%;background:var(--blue)}
.photo{position:absolute}
p{font-size:12.5px;line-height:23px}
.card{position:absolute;background:var(--white);box-shadow:0 4px 24px rgba(0,0,0,.12);padding:54px 36px 0}
.card h2{font-style:italic;font-weight:800;font-size:31px;color:var(--ink);margin-bottom:16px}
.quote{position:absolute;background:var(--blue-soft);font-style:italic;font-size:15px;line-height:29px;color:var(--ink);text-align:center;padding:24px 46px;display:flex;align-items:center;justify-content:center}
.quote-white{background:var(--white);box-shadow:0 4px 24px rgba(0,0,0,.1)}
.step{position:absolute;padding:18px 8px;font-size:12px;line-height:21px;color:var(--text)}
.step b{display:block;color:var(--ink);font-size:13px;margin-bottom:8px}
.foot h4{font-weight:600;font-size:17px;color:var(--white);margin-bottom:14px}
.foot p{color:#e8f5fc;font-size:12px;line-height:22px}
.social{display:flex;gap:6px}
.social span{width:32px;height:30px;border:1.5px solid #fff;display:flex;align-items:center;justify-content:center}
</style>
</head>
<body>

<header class="abs" style="left:0;top:0;width:1200px;height:76px;background:var(--white)">
  <div class="brand abs" style="left:141px;top:12px"><span class="brand-dot"></span>LQV</div>
  <svg class="abs" style="left:745px;top:22px" width="32" height="32" viewBox="0 0 32 32"><circle cx="16" cy="16" r="14" fill="none" stroke="var(--blue)" stroke-width="1.5"/><path d="M11 10c1-1 2-1 3 0l1 2c0 1-1 2-1 2 1 2 2 3 4 4 0 0 1-1 2-1l2 1c1 1 1 2 0 3-3 2-12-6-11-11z" fill="none" stroke="var(--blue)" stroke-width="1.3"/></svg>
  <div class="abs" style="left:788px;top:19px;font-size:13px;line-height:17px;color:var(--ink)">Phone<br>555.010.4780</div>
  <div class="btn" style="left:902px;top:18px;width:157px;height:39px">Contact Us Today</div>
</header>

<section class="photo" role="img" aria-label="Refinery at sunset with an engineer in a hard hat and safety vest working on a laptop" style="left:0;top:76px;width:1200px;height:494px;background:linear-gradient(180deg,#8fb3cf 0%,#b9c6cf 45%,#d9a56a 70%,#3a3a3c 100%)"></section>
<h1 class="abs" style="left:143px;top:238px;font-weight:600;font-size:56px;line-height:66px;color:var(--ink)">Distant Charting<br>&amp; Rostering</h1>

<div class="photo" role="img" aria-label="Stressed man at a desk holding his head beside a laptop" style="left:141px;top:641px;width:537px;height:394px;background:linear-gradient(135deg,#c9c7c2,#8c8a86)"></div>
<div class="card" style="left:522px;top:753px;width:537px;height:367px">
  <h2>The Problem</h2>
  <ol style="font-size:12.5px;line-height:25px;padding-left:24px;color:var(--text)">
    <li>High cost for turnaround planning and scheduling</li>
    <li>Safety risks, social distancing issues</li>
    <li>Legal liabilities, co-employment issues</li>
    <li>Distraction due to plant upsets, or site interferences</li>
  </ol>
  <p style="margin-top:4px">Iriure dolor in hendrerit in vulputate velit esse molestie consequat, vel illum dolor eu feugiat nulla facilisis at vero eros et accumsan et iusto odio dignissim.</p>
  <div class="btn" style="left:32px;top:268px;width:157px;height:38px">Get the Solution</div>
</div>

<div class="abs" style="left:290px;top:1183px;font-size:110px;font-weight:800;color:#f2f2f2;letter-spacing:4px;line-height:110px">SOLUTIONS</div>
<h2 class="abs" style="left:184px;top:1220px;font-style:italic;font-weight:800;font-size:31px;color:var(--ink)">General Solution</h2>
<div class="abs" style="left:466px;top:1218px;width:3px;height:44px;background:var(--blue)"></div>
<p class="abs" style="left:505px;top:1200px;width:520px;font-size:13px;line-height:27px;color:var(--ink)">A customizable solution that you pay for one time. That reduces the owner’s risk, is not impacted by site conditions or limitations, is transparent, and accountable for planning and scheduling turnarounds.</p>

<div class="quote" style="left:175px;top:1340px;width:850px;height:106px">
  Distant Charting and Rostering is a new way of providing the same process of developing job plans, work packages, and turnaround schedules for a fraction of the cost of conventional methods.
</div>

<section class="abs" style="left:0;top:1501px;width:1200px;height:1188px;background:var(--grey-band)">
  <h2 class="abs" style="left:0;width:1200px;top:112px;text-align:center;font-weight:400;font-size:39px;color:var(--ink)">How It Works</h2>
  <div class="abs" style="left:574px;top:168px;width:52px;height:2px;background:var(--blue)"></div>
  <div class="abs" style="left:584px;top:174px;width:32px;height:2px;background:var(--blue)"></div>

  <h3 class="abs" style="left:143px;top:316px;font-style:italic;font-weight:400;font-size:32px;color:var(--blue)">In General</h3>
  <div class="abs" style="left:143px;top:364px;width:345px">
    <p style="font-size:12px">LQV still follows all the industry rules for planning and scheduling.</p>
    <p style="font-size:12px;margin-top:3px">But we now are able to perform a large portion of the processes off-site / remotely.</p>
    <p style="font-size:12px;margin-top:3px">By doing this reduces cost, minitmizes client’s exposer to legal liabilities, and can improve efficiencies.</p>
  </div>
  <div class="abs" style="left:628px;top:237px;width:466px;height:356px;border:6px solid #d6dfe9"></div>
  <div class="photo" role="img" aria-label="Two people shaking hands over a contract with a small model house and keys" style="left:590px;top:272px;width:467px;height:288px;background:linear-gradient(135deg,#6f7f8f,#c9b9a4)"></div>

  <h3 class="abs" style="left:0;width:1200px;top:676px;text-align:center;font-weight:400;font-size:32px;color:var(--blue)">How LQV Works</h3>
  <div class="abs" style="left:0;width:1200px;top:718px;text-align:center;font-style:italic;font-weight:800;font-size:17px;color:var(--ink)">In Specific</div>

  <div class="step" style="left:143px;top:769px;width:218px;height:133px;background:var(--step-a)"><b>Step 1</b>An onsite team is to collects all the necessary information required to develop job plans.</div>
  <div class="step" style="left:376px;top:769px;width:217px;height:133px;background:var(--step-b)"><b>Step 2</b>Then share it with the remote team using a planning software that both sides can access</div>
  <div class="step" style="left:608px;top:769px;width:218px;height:133px;background:var(--step-a)"><b>Step 3</b>The remote team then uses the information and documents to establish job plans and work package</div>
  <div class="step" style="left:839px;top:769px;width:218px;height:133px;background:var(--step-b)"><b>Step 4</b>A scheduler can then develop a turnaround schedule from the completed job plans from WEN’s office.</div>
  <div class="step" style="left:143px;top:917px;width:218px;height:133px;background:var(--step-b)"><b>Step 5</b>By using current technology and some industry’s best tools</div>
  <div class="step" style="left:376px;top:917px;width:217px;height:133px;background:var(--step-a)"><b>Step 6</b>Everyone will be able to track performance, collaborate &amp; share information quickly &amp; easily.</div>
  <div class="step" style="left:608px;top:917px;width:218px;height:133px;background:var(--step-b)"><b>Step 7</b>All this for a fixed price per package</div>
  <div class="brand abs" style="left:868px;top:960px"><span class="brand-dot"></span>LQV</div>

  <div class="btn" style="left:522px;top:1075px;width:156px;height:38px">Contact Us Today</div>
</section>

<div class="photo" role="img" aria-label="Smiling construction worker in a hard hat holding a tablet" style="left:141px;top:2751px;width:537px;height:395px;background:linear-gradient(135deg,#c7d3dc,#8a93a0)"></div>
<div class="card" style="left:522px;top:2862px;width:537px;height:367px;padding-top:56px">
  <h2>Exclusive Benefits</h2>
  <p style="font-size:12px">Clients no longer have to struggle with the recruiting process and reviewing resumes to find the right candidates. LQV is able to attract top resources, that will consistently deliver a product that you will pay for once.</p>
  <p style="font-size:12px;margin-top:6px">No overtime or perdiem cost, just a simple fixed rate per package is all you wil have to pay. &nbsp;We will minimize our client’s exposure to legal liabilities and co-employment issues that do come up from time to time by having employees on site</p>
  <p style="font-size:12px;margin-top:6px">Smaller events will be able to take full advantage of a well-developed planning and scheduling process that would typically be too expensive</p>
</div>
<p class="abs" style="left:150px;top:3260px;width:900px;text-align:center;font-size:12px">The larger events can reduce the risk of cost overrun, reducing the size of their planning facilities. &nbsp;It also minimizes the opportunity for exposure to on-site injuries, widespread sicknesses, or other risks that come from having personnel on-site. &nbsp;it.</p>
<div class="quote quote-white" style="left:175px;top:3329px;width:850px;height:150px">
  No matter your situation, we have a solution customizable to fit your needs. Our staff is scalable to handle almost any situation. Let us know what you need, and we will provide you with a final product that you pay for when you are happy with
</div>

<section class="abs" style="left:0;top:3570px;width:1200px;height:324px;background:var(--cta-band)">
  <p class="abs" style="left:150px;top:76px;width:900px;text-align:center;font-style:italic;font-size:26px;line-height:40px;color:var(--ink)">Give WEN A Call And Ask About Our Distant Charting And Rostering Services And How We Can Provide A Solution For Your Next Turnaround &nbsp;That Will Create Savings For You.</p>
  <div class="btn" style="left:416px;top:226px;width:157px;height:39px">Contact Us Today</div>
  <div class="abs" style="left:583px;top:228px;font-size:25px;color:var(--ink)">Or</div>
  <div class="btn" style="left:622px;top:226px;width:156px;height:39px">
    <svg width="20" height="20" viewBox="0 0 32 32"><path d="M9 7c1-1 3-1 4 0l2 3c0 1-1 3-1 3 2 3 3 4 6 6 0 0 2-1 3-1l3 2c1 1 1 3 0 4-4 3-19-10-17-17z" fill="none" stroke="#fff" stroke-width="2"/></svg>555.010.4780</div>
</section>

<footer class="abs foot" style="left:0;top:3894px;width:1200px;height:390px;background:var(--blue)">
  <div class="abs" style="left:143px;top:80px;width:290px">
    <h4>About LQV</h4>
    <p>Iriure dolor in hendrerit in vulputate velit esse molestie consequat, vel illum doloreu feugiat nulla facilisis at vero eros et accumsan o odio dignissim. Iriure dolor in hendrerit in vulputate velit esse molestie consequat, vel illum dolo eu feugiat nulla facilisis at vero eros et accumsan et iusto odio dignissim iriure dolor in hendrerit.</p>
  </div>
  <div class="abs" style="left:498px;top:80px;width:320px">
    <h4>Contact Details</h4>
    <div style="display:flex;gap:14px;margin-bottom:14px"><svg width="30" height="30" viewBox="0 0 30 30"><circle cx="15" cy="15" r="13" fill="none" stroke="#fff"/><path d="M15 8a4 4 0 0 1 4 4c0 3-4 8-4 8s-4-5-4-8a4 4 0 0 1 4-4z" fill="none" stroke="#fff"/></svg><p>LQV Office<br>Street Name, City Name State Zipcode</p></div>
    <div style="display:flex;gap:14px;margin-bottom:14px"><svg width="30" height="30" viewBox="0 0 30 30"><circle cx="15" cy="15" r="13" fill="none" stroke="#fff"/><path d="M10 9c1-1 2-1 3 0l1 2c0 1-1 2-1 2 1 2 2 3 4 4 0 0 1-1 2-1l2 1c1 1 1 2 0 3-3 2-12-6-11-11z" fill="none" stroke="#fff"/></svg><p>Phone<br>555.010.4780</p></div>
    <div style="display:flex;gap:14px"><svg width="30" height="30" viewBox="0 0 30 30"><circle cx="15" cy="15" r="13" fill="none" stroke="#fff"/><rect x="9" y="11" width="12" height="9" fill="none" stroke="#fff"/><path d="M9 11l6 5 6-5" fill="none" stroke="#fff"/></svg><p>Email<br>inquiry@lqv-example.com</p></div>
  </div>
  <div class="brand abs" style="left:860px;top:110px;color:var(--white)"><span class="brand-dot" style="background:#fff"></span>LQV</div>
  <div class="abs social" style="left:889px;top:186px">
    <span aria-label="Website"><svg width="16" height="16" viewBox="0 0 16 16"><circle cx="8" cy="8" r="6.5" fill="none" stroke="#fff"/><path d="M1.5 8h13M8 1.5c-3 3.5-3 9.5 0 13M8 1.5c3 3.5 3 9.5 0 13" fill="none" stroke="#fff"/></svg></span>
    <span aria-label="Email"><svg width="16" height="16" viewBox="0 0 16 16"><rect x="2" y="4" width="12" height="8.5" fill="none" stroke="#fff"/><path d="M2 4l6 5 6-5" fill="none" stroke="#fff"/></svg></span>
    <span aria-label="Chat"><svg width="16" height="16" viewBox="0 0 16 16"><path d="M2.5 3h11v7.5H7l-3 2.5v-2.5H2.5z" fill="none" stroke="#fff"/></svg></span>
    <span aria-label="Share"><svg width="16" height="16" viewBox="0 0 16 16"><circle cx="4" cy="8" r="1.8" fill="#fff"/><circle cx="12" cy="4" r="1.8" fill="#fff"/><circle cx="12" cy="12" r="1.8" fill="#fff"/><path d="M4 8l8-4M4 8l8 4" stroke="#fff"/></svg></span>
  </div>
  <p class="abs" style="left:0;width:1200px;top:344px;text-align:center">Copyright © 2021 Distant Charting And Rostering. All Rights Reserved.</p>
</footer>

</body>
</html>
```